Flyer-Design für Karin Dossow
Zielgruppe
Ich bin psychologische Beraterin und Heilpraktikerin für Psychotherapie. Ich biete ein Coaching speziell für Mütter (meist Mütter mit neugeborenen Babys) an. Dieses Mütter-Coaching will ich bewerben. Die Flyer werden unter anderen an Ärzte und Hebammen weiter gegeben und dort in den Praxen ausliegen.
Aufgabenstellung
In meinem Logo herrschen die Farben orange und grau vor - es wäre schön, wenn sich diese Farben im Flyer wiederfinden würden - evtl. kombiniert mit mittelblau oder einem hellem grün.
Des weiteren möchte ich später Flyer im Din Lang Format (einseitig) mit anderen Angeboten erstellen. Das sollte mit dem Design dann auch möglich sein.
Der Schrifttyp soll bitte Arial sein, passend zum Logo. Ich habe bei Bildarko Fotos zu dem Thema erstanden, die ich stimmig finde. Diese Bilder sollten im Flyer genutzt werden.
Für diesen Flyer hätte ich gerne das Format: Falzblatt mit Wickelfalz - 279 x 219 mm

```html
<!DOCTYPE html>
<html lang="de">
<head>
<meta charset="utf-8">
<title>Karin Dossow – Coaching für Mütter</title>
<link rel="stylesheet" href="https://fonts.googleapis.com/css2?family=Arimo:wght@400;700&display=swap">
<style>
  :root {
    --stage: #ecebe8;
    --grey-light: #e4e4e4;
    --grey-mid: #d2d2d2;
    --grey-text: #6a6a6a;
    --ink: #2b2b2b;
    --orange-top: #ecae4e;
    --orange-bottom: #e39a36;
    --photo-light: #f0f1e8;
    --photo-warm: #d8b9a0;
    --photo-dark: #4a3f3a;
    --white: #ffffff;
  }
  * { box-sizing: border-box; margin: 0; padding: 0; }
  html, body {
    width: 1200px;
    height: 835px;
    overflow: hidden;
    background: var(--stage);
    font-family: "Arimo", Arial, sans-serif;
  }
  .flyer-cover {
    position: absolute;
    left: 415px;
    top: 22px;
    width: 370px;
    height: 790px;
    box-shadow: 0 6px 24px rgba(0,0,0,0.18);
    overflow: hidden;
  }
  .cover-shapes {
    position: absolute;
    inset: 0;
    width: 100%;
    height: 100%;
  }
  .brand {
    position: absolute;
    top: 36px;
    left: 0;
    width: 100%;
    text-align: center;
  }
  .brand-name {
    display: inline-flex;
    align-items: center;
    gap: 8px;
    font-size: 28px;
    font-weight: 400;
    color: var(--grey-text);
    letter-spacing: 0.5px;
  }
  .brand-dot {
    width: 10px;
    height: 10px;
    border-radius: 50%;
    background: var(--orange-bottom);
  }
  .brand-claim {
    margin-top: 10px;
    font-size: 17px;
    font-weight: 700;
    color: var(--orange-bottom);
    letter-spacing: 0.3px;
  }
  .brand-services {
    margin-top: 4px;
    font-size: 10.5px;
    color: var(--ink);
    letter-spacing: 0.4px;
  }
  .headline {
    position: absolute;
    left: 34px;
    top: 500px;
    color: var(--white);
    font-size: 33px;
    font-weight: 400;
    line-height: 1.22;
    letter-spacing: -1px;
    text-transform: uppercase;
  }
  .headline strong { font-weight: 700; }
</style>
</head>
<body>
  <article class="flyer-cover">
    <svg class="cover-shapes" viewBox="0 0 370 790" preserveAspectRatio="none">
      <defs>
        <linearGradient id="header-tone" x1="0" y1="0" x2="1" y2="1">
          <stop offset="0" stop-color="var(--grey-mid)"/>
          <stop offset="1" stop-color="var(--grey-light)"/>
        </linearGradient>
        <linearGradient id="photo-tone" x1="0" y1="0" x2="1" y2="1">
          <stop offset="0" stop-color="var(--photo-light)"/>
          <stop offset="0.55" stop-color="var(--photo-warm)"/>
          <stop offset="1" stop-color="var(--photo-dark)"/>
        </linearGradient>
        <linearGradient id="band-tone" x1="0" y1="0" x2="0" y2="1">
          <stop offset="0" stop-color="var(--orange-top)"/>
          <stop offset="1" stop-color="var(--orange-bottom)"/>
        </linearGradient>
      </defs>
      <rect class="photo-area" x="0" y="130" width="370" height="400" fill="url(#photo-tone)" role="img" aria-label="Foto: Mutter hält ihr schlafendes Baby an der Schulter"/>
      <path class="header-band" d="M0 0 H370 V152 Q200 200 0 172 Z" fill="url(#header-tone)"/>
      <path class="headline-band" d="M0 460 Q170 400 370 500 V790 H0 Z" fill="url(#band-tone)"/>
    </svg>

    <header class="brand">
      <div class="brand-name"><span class="brand-dot"></span>Karin Dossow</div>
      <p class="brand-claim">COACHING FÜR MÜTTER</p>
      <p class="brand-services">BEGLEITUNG - STÄRKUNG - BERATUNG</p>
    </header>

    <h1 class="headline">
      Das Baby ist da<br>
      und <strong>nichts</strong><br>
      ist mehr<br>
      wie es war!
    </h1>
  </article>
</body>
</html>
```